Tavern Business Card

I need a nice and sleek business card.

I need it to promote our website, our ratebook page, and or picthread page

Picthread would be: @marlowjoinery
website would be: www.marlowjoinery.example
ratebook would be: Marlow Joinery Inc (logo is fine)

Here are a list of service we offer.
1. Custom Kitchen Remodeling
2. Custom Bathroom Remodeling
3. Custom Closet Remodeling
4. Custom Bedroom Remodeling
5. Custom Bars
6. Custom Bookcases
7. Custom Staircases
8. Custom Ceilings

Please use the wording "Grain & Gable"
We also have been in business since 1992
and we have been serving the rich and famous since.

We do all types of designs, modern and renaissance.

Industry/Entity Type

Business

Contact Information for Business Card

Marlow Joinery, Inc.
58710 Bellamy Rd,. Unit 304-305
Fernvale, CA. 90000
Teodor Kell Varinsky - CEO
555-430-6628
marlowjoinery@postbox.example

```html
<!DOCTYPE html>
<html lang="en">
<head>
<meta charset="utf-8">
<title>Marlow Joinery Inc. — Business Card</title>
<link rel="stylesheet" href="https://fonts.googleapis.com/css2?family=Cinzel:wght@400;500&display=swap">
<style>
  :root {
    --backdrop: #2a1a12;
    --card: #1a0f08;
    --card-edge: #d9cbbd;
    --card-edge-dark: #6b5a4c;
    --gold: #c9b7a0;
    --gold-soft: #a8957e;
    --cream: #e8ddcf;
    --mark-faint: #3a3230;
  }
  * { margin: 0; padding: 0; box-sizing: border-box; }
  html, body { width: 1200px; height: 902px; overflow: hidden; }
  body {
    position: relative;
    background: var(--backdrop);
    font-family: "Cinzel", serif;
    font-weight: 400;
    color: var(--gold);
  }
  h1, h2, p { font-weight: 400; }
  .card {
    position: absolute;
    background: var(--card);
    border: 3px solid var(--card-edge);
    border-bottom-color: var(--card-edge-dark);
    border-right-color: var(--card-edge-dark);
    box-shadow: 0 6px 14px rgba(0,0,0,.45);
  }
  .card::after {
    content: "";
    position: absolute;
    left: 0; right: 0; bottom: 4px;
    border-top: 1px solid var(--gold-soft);
  }
  .card--front { left: 275px; top: 112px; width: 660px; height: 330px; }
  .card--back  { left: 277px; top: 519px; width: 661px; height: 332px; }

  .web-address {
    position: absolute; left: 6px; top: 14px;
    font-size: 10px; letter-spacing: .6px; color: var(--gold);
  }
  .brand-seal {
    position: absolute; left: 225px; top: 42px; width: 210px; height: 200px;
  }
  .company-name {
    position: absolute; left: 0; right: 0; top: 256px;
    text-align: center; font-size: 19px; letter-spacing: 4px; color: var(--cream);
  }
  .social-handle {
    position: absolute; right: 10px; top: 303px;
    font-size: 10px; letter-spacing: .6px; color: var(--gold);
  }

  .brand-watermark {
    position: absolute; left: 40px; top: 20px; width: 580px; height: 230px;
  }
  .person-title {
    position: absolute; left: 10px; top: 255px;
    font-size: 25px; letter-spacing: 2px; color: var(--gold-soft);
  }
  .contact-line {
    position: absolute; left: 10px; top: 296px;
    font-size: 10px; letter-spacing: .4px; color: var(--gold); white-space: nowrap;
  }
</style>
</head>
<body>
  <section class="card card--front">
    <p class="web-address">www.marlowjoinery.example</p>
    <svg class="brand-seal" viewBox="0 0 210 200" aria-hidden="true">
      <circle cx="105" cy="80" r="56" fill="none" stroke="var(--gold-soft)" stroke-width="2"/>
      <text x="105" y="178" text-anchor="middle" font-family="Cinzel, serif" font-size="16" letter-spacing="2" fill="var(--gold-soft)">Marlow Joinery</text>
    </svg>
    <h1 class="company-name">MARLOW JOINERY INC.</h1>
    <p class="social-handle">@MARLOWJOINERY</p>
  </section>

  <section class="card card--back">
    <svg class="brand-watermark" viewBox="0 0 580 230" aria-hidden="true">
      <text x="290" y="140" text-anchor="middle" font-family="Cinzel, serif" font-size="60" letter-spacing="4" fill="var(--mark-faint)">Marlow Joinery</text>
    </svg>
    <h2 class="person-title">Kell Varinsky - CEO</h2>
    <p class="contact-line">58710 Bellamy Rd,. Unit 304-305 Fernvale, CA. 90000 Teodor&nbsp; 555-430-6628 marlowjoinery@postbox.example</p>
  </section>
</body>
</html>
```